Lar Ferreirinha Banners Ads

We need to create 4 animated banners ads in GIF (3 arts for each banner) to Lar Ferreirinha Adwords Display Campaign
Lar Ferreirinha is an ecommerce in Brazil that sells high end home products.
It is a Branding Campaign, but we will add products images on it, so it has to be very sofisticated like the brand is.

We need 4 designs - 1 design for each size:

- Retângulo inline (300 X 250)
- Retângulo grande (336 x 280)
- Banner (468 x 60)
- Cabeçalho (728 x 90)

Please, find the briefing in pdf archive attached

Text we can work on th banners:

1 - Sofisticação com exclusividade para sua Casa!
2 - chique, exclusivo e encantador
3 - Encantador, sofisticado e exclusivo

The final image has to have Tessalvino´s Logo, Lar Ferreirinha´s logo and a call to action:

Confira nossos produtos exclusivos!

_________________________________________________________________
UPDATE

Please, for the colors, take the ones from pdf; (use more collors chics, silver and white, but not only this colors);
Don't forget the CALL TO ACTION " Confira nossos Produtos Exclusivos!"

If you'd like to meet the brand and the target, here is the page on Facebook: https://www.facebook.com/LarFerreirinhaHomeFerreirinha

But please, DO NOT COPY ANY OF THESE EXAMPLES ON THE PAGE.
We need something more executive.

Target Market(s)

Woman 30+
Trendy, modern, sofisticated, married or mum, cosmopolitan,
UPPERCLASS

Industry/Entity Type

Call

Font styles to use
Script
Other font styles liked:
• ColfaxTrial

Requirements
Must have
• Product images
Text
Product Image + Call to action on final layer with logos
As you will see the example in pdf archive attached
Nice to have
• frames
Should not have
• people
flowers
girlish drawing

```html
<!DOCTYPE html>
<html lang="pt-BR">
<head>
<meta charset="utf-8">
<title>Lar Ferreirinha – Banners Display</title>
<link rel="stylesheet" href="https://fonts.googleapis.com/css2?family=Overpass:wght@700;800&display=swap">
<style>
  :root {
    --stage: #efeae4;
    --white: #ffffff;
    --brand-grey: #8a8178;
    --cta-pink: #e0409a;
    --headline-red: #e8141c;
    --outline: #ffffff;
    --shadow: #1a1a1a;
    --photo-wall: #6f7378;
    --photo-linen: #dcdcdc;
    --photo-pink: #e7c3cc;
    --photo-grey: #a9adb3;
    --scale: 1.172;
  }
  * { margin: 0; padding: 0; box-sizing: border-box; }
  html, body { width: 1200px; height: 900px; overflow: hidden; }
  body { background: var(--stage); font-family: "Overpass", Arial, sans-serif; position: relative; }

  .ad {
    position: absolute;
    overflow: hidden;
    background: var(--white);
    transform: scale(var(--scale));
    transform-origin: top left;
  }
  .ad-leaderboard { left: 270px; top: 279px; width: 728px; height: 90px; }
  .ad-banner      { left: 422px; top: 429px; width: 468px; height: 60px; }
  .ad-inline      { left: 345px; top: 564px; width: 300px; height: 250px; }
  .ad-large       { left: 748px; top: 546px; width: 336px; height: 280px; }

  .product-photo {
    position: absolute;
    background:
      linear-gradient(180deg, transparent 0%, transparent 55%, rgba(169,173,179,.9) 100%),
      radial-gradient(ellipse at 70% 35%, var(--photo-pink) 0%, rgba(231,195,204,.4) 30%, transparent 55%),
      linear-gradient(90deg, var(--photo-wall) 0%, #8d9095 18%, var(--photo-linen) 32%, #eeeeee 60%, var(--photo-grey) 100%);
  }

  .brand-name {
    position: absolute;
    color: var(--brand-grey);
    font-weight: 800;
    letter-spacing: .03em;
    white-space: nowrap;
    text-transform: uppercase;
    text-align: center;
  }

  .pointer { position: absolute; }

  .cta {
    position: absolute;
    background: var(--cta-pink);
    color: var(--white);
    font-weight: 700;
    text-align: center;
    line-height: 1.05;
    display: flex;
    align-items: center;
    justify-content: center;
  }

  .headline {
    position: absolute;
    color: var(--headline-red);
    font-weight: 800;
    text-align: center;
    line-height: 1.08;
    white-space: nowrap;
    text-shadow:
      -1px -1px 0 var(--outline), 1px -1px 0 var(--outline),
      -1px 1px 0 var(--outline), 1px 1px 0 var(--outline),
      0 -1px 0 var(--outline), 0 1px 0 var(--outline),
      -1px 0 0 var(--outline), 1px 0 0 var(--outline),
      3px 3px 0 var(--shadow);
  }

  /* 728 x 90 */
  .ad-leaderboard .product-photo { left: 167px; top: 0; width: 561px; height: 90px; }
  .ad-leaderboard .brand-name { left: 0; width: 167px; top: 38px; font-size: 13.5px; }
  .ad-leaderboard .pointer { left: 167px; top: 28px; width: 10px; height: 18px; }
  .ad-leaderboard .cta {
    left: 167px; top: 56px; width: 232px; height: 34px; font-size: 11.5px;
    clip-path: polygon(0 0, 88% 0, 100% 100%, 0 100%);
    padding-right: 18px;
  }
  .ad-leaderboard .headline { left: 392px; top: 10px; width: 140px; font-size: 20px; }

  /* 468 x 60 */
  .ad-banner .product-photo { left: 107px; top: 0; width: 361px; height: 60px; }
  .ad-banner .brand-name { left: 0; width: 107px; top: 25px; font-size: 8.5px; }
  .ad-banner .pointer { left: 107px; top: 18px; width: 7px; height: 12px; }
  .ad-banner .cta {
    left: 107px; top: 36px; width: 150px; height: 24px; font-size: 7.5px;
    clip-path: polygon(0 0, 86% 0, 100% 100%, 0 100%);
    padding-right: 14px;
  }
  .ad-banner .headline { left: 240px; top: 8px; width: 110px; font-size: 10.5px; text-shadow:
      -1px -1px 0 var(--outline), 1px -1px 0 var(--outline),
      -1px 1px 0 var(--outline), 1px 1px 0 var(--outline),
      2px 2px 0 var(--shadow); }

  /* 300 x 250 */
  .ad-inline .product-photo { left: 0; top: 37px; width: 300px; height: 213px; }
  .ad-inline .brand-name { left: 0; width: 300px; top: 5px; font-size: 26px; }
  .ad-inline .pointer { left: 140px; top: 36px; width: 20px; height: 11px; }
  .ad-inline .cta {
    left: 0; top: 197px; width: 212px; height: 36px; font-size: 12px;
    clip-path: polygon(0 0, 86% 0, 100% 100%, 0 100%);
    padding-right: 24px;
  }
  .ad-inline .headline { left: 2px; top: 78px; width: 144px; font-size: 16px; }

  /* 336 x 280 */
  .ad-large .product-photo { left: 0; top: 46px; width: 336px; height: 234px; }
  .ad-large .brand-name { left: 0; width: 336px; top: 7px; font-size: 29px; }
  .ad-large .pointer { left: 156px; top: 45px; width: 22px; height: 12px; }
  .ad-large .cta {
    left: 0; top: 222px; width: 238px; height: 40px; font-size: 13px;
    clip-path: polygon(0 0, 86% 0, 100% 100%, 0 100%);
    padding-right: 26px;
  }
  .ad-large .headline { left: 2px; top: 86px; width: 164px; font-size: 18px; }
</style>
</head>
<body>

  <section class="ad ad-leaderboard" aria-label="Cabeçalho 728 x 90">
    <div class="product-photo" role="img" aria-label="Cama com roupa de cama cinza e almofadas rosa e brancas"></div>
    <span class="brand-name">Lar Ferreirinha</span>
    <svg class="pointer" viewBox="0 0 10 18" aria-hidden="true"><polygon points="0,0 10,9 0,18" fill="#ffffff"/></svg>
    <p class="cta">Confira nossos Produtos<br>Exclusivos!</p>
    <p class="headline">Encantador,<br>sofisticado<br>e exclusivo</p>
  </section>

  <section class="ad ad-banner" aria-label="Banner 468 x 60">
    <div class="product-photo" role="img" aria-label="Cama com roupa de cama cinza e almofadas rosa e brancas"></div>
    <span class="brand-name">Lar Ferreirinha</span>
    <svg class="pointer" viewBox="0 0 7 12" aria-hidden="true"><polygon points="0,0 7,6 0,12" fill="#ffffff"/></svg>
    <p class="cta">Confira nossos Produtos<br>Exclusivos!</p>
    <p class="headline">Sofisticação com<br>exclusividade<br>para sua Casa!</p>
  </section>

  <section class="ad ad-inline" aria-label="Retângulo inline 300 x 250">
    <div class="product-photo" role="img" aria-label="Cama com roupa de cama cinza e almofadas rosa e brancas"></div>
    <span class="brand-name">Lar Ferreirinha</span>
    <svg class="pointer" viewBox="0 0 20 11" aria-hidden="true"><polygon points="0,0 20,0 10,11" fill="#ffffff"/></svg>
    <p class="headline">Sofisticação com<br>exclusividade<br>para sua Casa!</p>
    <p class="cta">Confira nossos Produtos<br>Exclusivos!</p>
  </section>

  <section class="ad ad-large" aria-label="Retângulo grande 336 x 280">
    <div class="product-photo" role="img" aria-label="Cama com roupa de cama cinza e almofadas rosa e brancas"></div>
    <span class="brand-name">Lar Ferreirinha</span>
    <svg class="pointer" viewBox="0 0 22 12" aria-hidden="true"><polygon points="0,0 22,0 11,12" fill="#ffffff"/></svg>
    <p class="headline">Sofisticação com<br>exclusividade<br>para sua Casa!</p>
    <p class="cta">Confira nossos Produtos<br>Exclusivos!</p>
  </section>

</body>
</html>
```